Business Card Design Project

We need a business card design for a new company based in Singapore called 'Bright Harbor Pte Ltd'. We provide personal development training and emotional intelligence workshops. Our slogan is "Actualize your potentials". We will not have a company address on the business card. Only phone number, email address and website address.

Target Market(s)

Adults age 25 to 45 years old.
Mostly working in a job.

Industry/Entity Type

Training

Colors
0255a2
f37123

```html
<!DOCTYPE html>
<html lang="en">
<head>
<meta charset="utf-8">
<title>Bright Harbor Pte Ltd – Business Card</title>
<link rel="stylesheet" href="https://fonts.googleapis.com/css2?family=Michroma&family=Sacramento&display=swap">
<style>
  :root {
    --page: #ffffff;
    --card: #0255a2;
    --ink: #ffffff;
    --accent: #f37123;
  }
  * { margin: 0; padding: 0; box-sizing: border-box; }
  html, body {
    width: 848px;
    height: 1200px;
    overflow: hidden;
    background: var(--page);
  }
  .sheet {
    position: relative;
    width: 848px;
    height: 1200px;
  }
  .card {
    position: absolute;
    left: 41px;
    width: 760px;
    height: 460px;
    background: var(--card);
    overflow: hidden;
  }
  .card--front { top: 84px; }
  .card--back { top: 563px; }

  .emblem {
    position: absolute;
    left: 190px;
    top: 63px;
    width: 382px;
    height: 338px;
  }

  .brand {
    position: absolute;
    left: 0;
    top: 0;
    width: 100%;
    height: 170px;
    font-weight: 400;
    color: var(--ink);
  }
  .brand__name {
    position: absolute;
    left: 0;
    width: 100%;
    top: 22px;
    text-align: center;
    font-family: "Sacramento", cursive;
    font-size: 86px;
    line-height: 110px;
  }
  .brand__suffix {
    position: absolute;
    right: 114px;
    top: 146px;
    font-family: "Michroma", sans-serif;
    font-size: 14px;
    line-height: 16px;
    letter-spacing: 0.5px;
    color: var(--accent);
  }

  .contact {
    position: absolute;
    left: 0;
    width: 100%;
    top: 226px;
    list-style: none;
    text-align: center;
    font-family: "Michroma", sans-serif;
    font-size: 22px;
    line-height: 29px;
    letter-spacing: 0.6px;
    color: var(--ink);
  }

  .slogan {
    position: absolute;
    left: 0;
    width: 100%;
    top: 376px;
    text-align: center;
    font-family: "Sacramento", cursive;
    font-size: 44px;
    line-height: 54px;
    color: var(--accent);
  }
</style>
</head>
<body>
  <main class="sheet">
    <section class="card card--front">
      <svg class="emblem" viewBox="0 0 382 338" role="img" aria-label="Brand emblem illustration area">
        <rect width="382" height="338" fill="var(--accent)"/>
      </svg>
    </section>

    <section class="card card--back">
      <h1 class="brand">
        <span class="brand__name">Bright Harbor</span>
        <span class="brand__suffix">PTE Ltd</span>
      </h1>
      <ul class="contact">
        <li>CONTACT DETAILS GO HERE</li>
        <li>CONTACT DETAILS GO HERE</li>
        <li>CONTACT DETAILS GO HERE</li>
        <li>CONTACT DETAILS GO HERE</li>
      </ul>
      <p class="slogan">Actualize your potentials</p>
    </section>
  </main>
</body>
</html>
```